Tarn Business Card Design Project

We have an existing business card. We are looking to creat a new card for the store. I have attached a my own business so you have a refference of what the current card looks like.

Phone: 1300 571 342
email: kelwood@tarnglazing.com.au
website: www.tarnglazing.com.au
Address: (Inside Kelwood Flooring Yard) 214 Farrow Rd, Ashwick VIC 3192
Updates

This is a new business card for our store.

Industry/Entity Type

Business

Requirements
Must have
• Must look similar to the existing card

```html
<!DOCTYPE html>
<html lang="en">
<head>
<meta charset="utf-8">
<title>Tarn Shutters &amp; Blinds – Business Card</title>
<link rel="stylesheet" href="https://fonts.googleapis.com/css2?family=Open+Sans:wght@400;600&family=Arimo:wght@700&display=swap">
<style>
  :root{
    --backdrop:#e9e7e3;
    --card:#ffffff;
    --card-edge:#3a3a3a;
    --ink:#231f20;
    --tagline:#6d6e71;
    --muted:#6a6a6a;
    --rule:#c4c4c4;
  }
  *{margin:0;padding:0;box-sizing:border-box}
  html,body{width:1200px;height:1167px;overflow:hidden}
  body{background:var(--backdrop);position:relative;font-family:"Open Sans",Arial,sans-serif;color:var(--ink)}

  .card{position:absolute;width:896px;height:511px;background:var(--card);border:1.5px solid var(--card-edge);border-radius:38px}
  .card--front{left:256px;top:38px}
  .card--back{left:38px;top:603px}

  .block{position:absolute;left:0;width:100%;text-align:center;white-space:nowrap}

  .wordmark{font-family:"Open Sans",Arial,sans-serif;font-weight:600;font-size:180px;line-height:1;letter-spacing:-3px;color:var(--ink)}
  .card--front .wordmark{top:35px}
  .card--back .wordmark{top:136px}

  .tagline{font-family:"Arimo",Arial,sans-serif;font-weight:700;font-size:40px;line-height:1;color:var(--tagline);letter-spacing:.5px}
  .card--front .tagline{top:220px}
  .card--back .tagline{top:324px}

  .person{top:292px;font-size:28px;line-height:1}
  .person__name{font-weight:600}
  .person__role{font-size:23px;color:var(--muted)}

  .divider{position:absolute;left:74px;width:764px;top:349px;height:3px;border-radius:2px;
    background:linear-gradient(90deg,rgba(196,196,196,0),var(--rule) 8%,var(--rule) 92%,rgba(196,196,196,0))}

  .contact{font-size:23px;line-height:1;display:flex;justify-content:center;align-items:center;gap:10px}
  .contact svg{width:20px;height:20px;flex:none}
  .contact--phone{top:375px}
  .contact--online{top:410px;gap:8px}
  .contact--online .spacer{width:10px}
  .address{top:460px;font-size:21px;line-height:1}

  .web{top:410px;font-size:30px;line-height:1;letter-spacing:4px}
</style>
</head>
<body>

<section class="card card--front" aria-label="Business card front">
  <div class="block wordmark">tarn</div>
  <div class="block tagline">Shutters &amp; Blinds</div>
  <div class="block person"><span class="person__name">Daniel Hart,</span> <span class="person__role">Director</span></div>
  <div class="divider"></div>

  <div class="block contact contact--phone">
    <svg viewBox="0 0 20 20" aria-hidden="true"><circle cx="10" cy="10" r="8.5" fill="none" stroke="#555" stroke-width="1.3"/><path d="M7.3 5.5c-.9 2.8-.3 6.3 2.4 9l1.3-1.6-1.5-1.8-.8.4c-.8-1.2-1-2.6-.7-3.9l.9.1.7-2.2z" fill="#555"/></svg>
    <span>1300 571 342</span>
  </div>

  <div class="block contact contact--online">
    <svg viewBox="0 0 20 20" aria-hidden="true"><path d="M2 8l8-5 8 5v8H2z" fill="#555"/><path d="M2 8l8 5 8-5" fill="none" stroke="#fff" stroke-width="1.2"/></svg>
    <span>kelwood@tarnglazing.com.au</span>
    <span class="spacer"></span>
    <svg viewBox="0 0 20 20" aria-hidden="true"><g fill="none" stroke="#555" stroke-width="1.1"><circle cx="10" cy="10" r="8.5"/><ellipse cx="10" cy="10" rx="4" ry="8.5"/><path d="M1.5 10h17M3 5.5h14M3 14.5h14M10 1.5v17"/></g></svg>
    <span>www.tarnglazing.com.au</span>
  </div>

  <div class="block address">214 Farrow Rd, Ashwick VIC 3192</div>
</section>

<section class="card card--back" aria-label="Business card back">
  <div class="block wordmark">tarn</div>
  <div class="block tagline">Shutters &amp; Blinds</div>
  <div class="block web">www.tarnglazing.com.au</div>
</section>

</body>
</html>
```